Harlow Custom Craft Website update

I would like an updated website to my current site (Harlowcraft.com).
I have an updated logo i would like to incorporate.
24 pages , would like to integrate videos of the boats (that i can upload later)

Target Market(s)

Professional and Commercial boat owners

Industry/Entity Type

Custom Boat Manufacturing

Coding

Coded - Design and coding required

Number of Pages Required

5+ page

Font styles to use
Serif

Requirements
Must have
• Easy to read, well laid-out, and video integration
Nice to have
• Fresh up to date look

```html
<!DOCTYPE html>
<html lang="en">
<head>
<meta charset="utf-8">
<title>Harlow Custom Craft</title>
<link href="https://fonts.googleapis.com/css2?family=Lato:wght@400;700&family=Racing+Sans+One&display=swap" rel="stylesheet">
<style>
:root{
  --navy:#0a3aa0;
  --navy-deep:#062a7a;
  --red:#c8202a;
  --ink:#222;
  --text:#3a3a3a;
  --pale:#d8e6fb;
  --white:#fff;
  --footer:#0b0b0b;
}
*{margin:0;padding:0;box-sizing:border-box}
html,body{width:1200px;height:3662px;overflow:hidden}
body{position:relative;background:var(--white);font-family:'Lato',sans-serif;color:var(--text)}
.abs{position:absolute}
.display{font-family:'Racing Sans One',sans-serif;font-style:italic;letter-spacing:1px}
.accent-bar{position:absolute;height:6px;width:226px;background:var(--red);border-radius:50%}
.btn{position:absolute;display:flex;align-items:center;justify-content:center;color:#fff;font-weight:700;font-size:17px;background:var(--navy);clip-path:polygon(8% 0,100% 0,92% 100%,0 100%);border-radius:0 14px 0 14px}

/* hero */
.hero{left:0;top:0;width:1200px;height:630px;background:linear-gradient(180deg,#6f9cc4 0%,#a9c7df 30%,#dcc6a0 58%,#4f88b6 72%,#1f5f93 100%)}
.hero-curve{left:0;top:0}
.site-header{left:111px;top:7px;width:977px;height:81px;background:#fff;border-radius:6px}
.brand{position:absolute;left:22px;top:24px;font-weight:700;font-size:22px;color:var(--navy);display:flex;align-items:center;gap:8px}
.brand .dot{width:12px;height:12px;background:var(--red)}
.nav{position:absolute;left:288px;top:37px;display:flex;gap:22px;font-size:15px;color:var(--ink)}
.nav .active{color:var(--red);text-decoration:underline}
.nav-cta{position:absolute;right:14px;top:18px;width:176px;height:46px;font-size:17px}
.hero-title{left:108px;top:160px;color:#fff;font-size:50px;line-height:64px;text-shadow:0 2px 4px rgba(0,0,0,.35)}
.hero-text{left:112px;top:307px;width:500px;color:#fff;font-size:15px;line-height:27px}
.hero-btn{left:114px;top:400px;width:177px;height:46px}

/* section heading */
.heading{font-size:38px;color:var(--navy)}
.heading .red{color:var(--red)}

.photo{position:absolute}
.body-copy{font-size:15px;line-height:26.6px;color:var(--text)}

/* boats */
.boats{left:0;top:1208px;width:1200px;height:586px;background:var(--pale)}
.card{position:absolute;top:174px;width:307px;height:323px;border-radius:8px;overflow:hidden}
.card-label{position:absolute;left:0;bottom:0;width:100%;height:62px;background:var(--navy);color:#fff;font-size:22px;display:flex;align-items:center;justify-content:center;clip-path:polygon(14% 0,100% 0,100% 100%,0 100%,0 60%);border-radius:0 0 30px 0}
.arrow{position:absolute;top:316px;width:32px;height:32px;border-radius:50%;display:flex;align-items:center;justify-content:center}

/* brands */
.partner{position:absolute;top:2050px;width:220px;text-align:center;font-weight:700;font-size:30px;color:#111;letter-spacing:1px}

/* footer */
.footer{left:0;top:3303px;width:1200px;height:359px;background:var(--footer);color:#fff}
.footer-brand{position:absolute;left:111px;top:110px;font-weight:700;font-size:22px;color:#fff}
.socials{position:absolute;left:111px;top:228px;display:flex;gap:12px}
.socials span{width:28px;height:28px;border-radius:50%;background:#fff;display:block}
.socials span:first-child{background:var(--red)}
.fcol{position:absolute;top:85px}
.fcol h4{font-family:'Racing Sans One',sans-serif;font-style:italic;color:var(--red);font-size:21px;font-weight:400;margin-bottom:6px}
.fcol ul{list-style:none;font-size:15px;line-height:28px}
.fcol li::before{content:"";display:inline-block;width:8px;height:8px;background:var(--red);margin:0 12px 1px 0}
.contact-row{display:flex;align-items:flex-start;gap:10px;font-size:15px;line-height:26px;margin-bottom:12px}
.contact-row svg{flex:none;margin-top:3px}
.footer-rule{position:absolute;left:111px;top:310px;width:977px;height:1px;background:#444}
.copyright{position:absolute;left:0;top:326px;width:1200px;text-align:center;font-size:15px}
</style>
</head>
<body>

<!-- Hero -->
<section class="abs hero" role="img" aria-label="Photo of an orange and white research vessel on calm sea at sunrise"></section>
<svg class="abs hero-curve" width="1200" height="640" viewBox="0 0 1200 640" aria-hidden="true">
  <path d="M0 590 Q420 640 880 600 Q1130 560 1200 330 L1200 640 L0 640 Z" fill="#fff"/>
  <path d="M170 604 Q560 640 880 612 Q1140 575 1200 340 L1200 305 Q1150 540 880 596 Q560 630 170 604 Z" fill="var(--navy)"/>
</svg>

<header class="abs site-header">
  <div class="brand"><span class="dot"></span>Harlow Custom Craft</div>
  <nav class="nav">
    <span class="active">Home</span><span>Boats</span><span>Coast Guard Package</span><span>Links</span><span>Driving Directions</span>
  </nav>
  <a class="btn nav-cta">Contact Us</a>
</header>

<h1 class="abs display hero-title">Engineered for Excellence.<br>Crafted for You.</h1>
<p class="abs hero-text">We build custom boats to meet our customers' specification. Our boats range in size from 26' to 71'. We specialize in Dive Boats, Yacht Sport</p>
<a class="btn hero-btn">Get Started</a>

<!-- About -->
<svg class="photo" style="left:111px;top:707px" width="468" height="413" viewBox="0 0 468 413" role="img" aria-label="Photo of a white custom vessel at sea under a cloudy sky">
  <defs><linearGradient id="gAbout" x1="0" y1="0" x2="0" y2="1"><stop offset="0" stop-color="#a9c2d8"/><stop offset=".55" stop-color="#d9dee2"/><stop offset=".7" stop-color="#4b6f8f"/><stop offset="1" stop-color="#1f3c57"/></linearGradient></defs>
  <path d="M30 0 H468 V190 Q460 400 250 413 H0 Z" fill="url(#gAbout)"/>
</svg>
<div class="accent-bar" style="left:765px;top:720px"></div>
<h2 class="abs display heading" style="left:642px;top:738px">About Harlow <span class="red">Boats</span></h2>
<p class="abs body-copy" style="left:644px;top:805px;width:450px">Harlow Custom Craft is a premier manufacturer of custom boats, specializing in the creation of high-quality vessels ranging from 28 to 72 feet in length. With a strong focus on precision and craftsmanship, we design and build boats tailored to meet the diverse needs of our clients. Our portfolio spans a wide array of markets, featuring everything from sleek recreational fishing boats, ready for adventures on the water, to robust commercial diving vessels designed to thrive in the toughest conditions. Regardless of</p>
<a class="btn" style="left:644px;top:1053px;width:176px;height:46px">Read More</a>

<!-- Our Boats -->
<section class="abs boats">
  <div class="accent-bar" style="left:487px;top:86px"></div>
  <h2 class="abs display heading" style="left:0;width:1200px;text-align:center;top:106px">Our <span class="red">Boats</span></h2>
  <div class="card" style="left:111px">
    <div role="img" aria-label="Photo of a white dive boat on turquoise water" style="width:100%;height:100%;background:linear-gradient(180deg,#7c96b4 0%,#c9d3dd 45%,#f2f2f2 60%,#4fa9b6 80%,#2e8c9c 100%)"></div>
    <div class="card-label display">Dive Boats</div>
  </div>
  <div class="card" style="left:445px">
    <div role="img" aria-label="Photo of a white patrol boat moored by a tree-lined shore" style="width:100%;height:100%;background:linear-gradient(180deg,#bcc8d4 0%,#cfd8df 25%,#3d5a37 45%,#e6e6e6 60%,#7a8a8f 78%,#55676d 100%)"></div>
    <div class="card-label display">Patrol Boats</div>
  </div>
  <div class="card" style="left:781px">
    <div role="img" aria-label="Photo of a red and white offshore fishing vessel with cranes" style="width:100%;height:100%;background:linear-gradient(180deg,#5c86bb 0%,#9fb9d8 40%,#c8323a 62%,#2c5b8f 75%,#1d4575 100%)"></div>
    <div class="card-label display" style="font-size:20px">Yacht Sport Fisherman</div>
  </div>
  <div class="arrow" style="left:46px;background:var(--red)"><svg width="14" height="14" viewBox="0 0 14 14"><path d="M9 2 4 7l5 5" stroke="#fff" stroke-width="2.4" fill="none"/></svg></div>
  <div class="arrow" style="left:1131px;background:#555"><svg width="14" height="14" viewBox="0 0 14 14"><path d="M5 2l5 5-5 5" stroke="#fff" stroke-width="2.4" fill="none"/></svg></div>
</section>

<!-- Brands -->
<div class="accent-bar" style="left:487px;top:1878px"></div>
<h2 class="abs display heading" style="left:0;width:1200px;text-align:center;top:1896px">Trusted Brands. <span class="red">Proven Performance</span></h2>
<div class="partner" style="left:116px">KESTREL</div>
<div class="partner" style="left:367px">IRONBANK</div>
<div class="partner" style="left:616px">MERIDIAN</div>
<div class="partner" style="left:870px">FIELDSTONE</div>

<!-- Video -->
<section class="abs" style="left:0;top:2225px;width:1200px;height:489px;background:radial-gradient(ellipse at 20% 25%,#5d7890 0%,#1d3646 40%,#10232f 100%)" role="img" aria-label="Aerial video still of a boat speeding across dark water leaving a white wake">
  <svg class="abs" style="left:563px;top:181px" width="90" height="90" viewBox="0 0 90 90" aria-hidden="true">
    <circle cx="45" cy="45" r="45" fill="rgba(200,200,200,.55)"/>
    <path d="M34 28 L64 45 L34 62 Z" fill="var(--red)"/>
  </svg>
</section>

<!-- Research vessels -->
<div class="accent-bar" style="left:190px;top:2828px"></div>
<h2 class="abs display heading" style="left:111px;top:2846px">research <span class="red">vessels</span></h2>
<p class="abs body-copy" style="left:111px;top:2912px;width:460px">In addition to research vessels, we specialize in durable supply boats essential for efficient logistics in remote areas. Our buoy tender boats, designed for the Coastal Marine Survey Office (CMSO), aid in the maintenance and deployment of buoys that are critical for environmental monitoring. Furthermore, we create specialized dive boats customized for specific regions, ensuring they meet the unique demands of local diving activities.</p>
<a class="btn" style="left:111px;top:3131px;width:177px;height:46px">Read More</a>
<svg class="photo" style="left:642px;top:2804px" width="470" height="412" viewBox="0 0 470 412" role="img" aria-label="Photo of a dark-hulled research vessel cutting through open water">
  <defs><linearGradient id="gRes" x1="0" y1="0" x2="0" y2="1"><stop offset="0" stop-color="#5f8fc6"/><stop offset=".45" stop-color="#9ab8d8"/><stop offset=".6" stop-color="#2d4a66"/><stop offset="1" stop-color="#173552"/></linearGradient></defs>
  <path d="M30 0 H470 Q465 60 458 150 Q440 400 250 412 H0 Z" fill="url(#gRes)"/>
</svg>

<!-- Footer -->
<footer class="abs footer">
  <div class="footer-brand">Harlow Custom Craft</div>
  <div class="socials"><span></span><span></span><span></span></div>

  <div class="fcol" style="left:380px">
    <h4>Quick Links</h4>
    <ul><li>Home</li><li>Boats</li><li>Coast Guard Package</li><li>Links</li><li>Driving Directions</li></ul>
  </div>
  <div class="fcol" style="left:593px">
    <h4>Our Models</h4>
    <ul><li>71' Custom Dive</li><li>58' Dive Special</li><li>53' Sport Fish</li><li>53' Dive/Excursion</li><li>46' Dive Special</li></ul>
  </div>
  <div class="fcol" style="left:812px">
    <h4>Contact Us</h4>
    <div class="contact-row"><svg width="22" height="22" viewBox="0 0 22 22"><circle cx="11" cy="11" r="11" fill="var(--red)"/><path d="M7 6c1 0 1.5 2 1.5 2.5S7.5 9.5 8 10.5s2 2.5 3.5 3.5c1 .5 1.5-.5 2-.5s2.5.5 2.5 1.5-1 1.5-2 1.5C10 16 6 12 6 8c0-1 .5-2 1-2Z" fill="#fff"/></svg>555.210.4417</div>
    <div class="contact-row"><svg width="22" height="22" viewBox="0 0 22 22"><circle cx="11" cy="11" r="11" fill="var(--red)"/><rect x="6" y="7.5" width="10" height="7" fill="none" stroke="#fff" stroke-width="1.4"/><path d="M6 7.5 11 11.5 16 7.5" fill="none" stroke="#fff" stroke-width="1.4"/></svg>office@harlowcraft.com</div>
    <div class="contact-row"><svg width="22" height="24" viewBox="0 0 22 24"><path d="M11 1a8 8 0 0 0-8 8c0 6 8 14 8 14s8-8 8-14a8 8 0 0 0-8-8Z" fill="var(--red)"/><circle cx="11" cy="9" r="3" fill="#fff"/></svg><span>Harlow Craft, Inc.&nbsp; 4120 Harbor Rd.<br>Port Linden, Louisiana&nbsp; 70999</span></div>
  </div>

  <div class="footer-rule"></div>
  <p class="copyright">Copyright © 2025 Harlow Craft. All rights reserved.</p>
</footer>

</body>
</html>
```